Financial Planning Pyramid Graphic

I need a graphic of a pyramid including 3 levels.

I've attached a copy of the article to be published with the graphic.

Also attached company logos if it makes sense to use.

See www.CorvallePrivateAdvisors.com for a general reference.

Target Market(s)

small and medium size business owners who intend to eventually sell their business. primarily servicing the construction, real estate, and technology industries.

Industry/Entity Type

Financial Planning

Font styles to use
Sans Serif

Requirements
Must have
• Primary branding hex color #009b81

Three levels of the pyramid:
3. Top: Wealth Distribution
2. Middle: Growing Wealth
1. Base: Protection (Risk Management)

It should somehow show how "Tax Planning" permeates all 3 layers.
Nice to have
• The attached article includes details about what the graphic should represent and more details that may be included.

```html
<!DOCTYPE html>
<html lang="en">
<head>
<meta charset="utf-8">
<title>Financial Planning Pyramid – Corvalle Private Advisors</title>
<link rel="stylesheet" href="https://fonts.googleapis.com/css2?family=Open+Sans:wght@300;400;700;800&display=swap">
<style>
  :root {
    --brand: #009b81;
    --teal-mid: #18705f;
    --teal-deep: #1b4a55;
    --pillar-dark: #123e48;
    --pillar-mid: #0e5e52;
    --pillar-light: #0a7b67;
    --face-top-left: #0a7d69;
    --face-top-front: #12a089;
    --face-mid-left: #0d5f52;
    --face-mid-front: #1a7465;
    --face-base-left: #123a45;
    --face-base-front: #1c4b56;
    --edge: #5fc2b2;
    --seam: #0b3138;
    --ink: #222222;
    --white: #ffffff;
    --bg: #ffffff;
  }
  html, body {
    margin: 0;
    padding: 0;
    width: 1199px;
    height: 1200px;
    overflow: hidden;
    background: var(--bg);
  }
  .artboard {
    display: block;
    width: 1199px;
    height: 1200px;
    font-family: "Open Sans", Arial, sans-serif;
  }
  .pillar-dark { fill: var(--pillar-dark); }
  .pillar-mid { fill: var(--pillar-mid); }
  .pillar-light { fill: var(--pillar-light); }
  .band-top { fill: var(--brand); }
  .band-mid { fill: var(--teal-mid); }
  .band-base { fill: var(--teal-deep); }
  .face { stroke: var(--edge); stroke-width: 1.5; stroke-linejoin: round; }
  .face-top-left { fill: var(--face-top-left); }
  .face-top-front { fill: var(--face-top-front); }
  .face-mid-left { fill: var(--face-mid-left); }
  .face-mid-front { fill: var(--face-mid-front); }
  .face-base-left { fill: var(--face-base-left); }
  .face-base-front { fill: var(--face-base-front); }
  .tier-seam { fill: none; stroke: var(--seam); stroke-width: 5; stroke-linejoin: round; }
  .tier-note {
    fill: var(--white);
    font-weight: 800;
    font-size: 15px;
    letter-spacing: 0.8px;
  }
  .band-label {
    fill: var(--white);
    font-weight: 700;
    font-size: 21px;
    letter-spacing: 2px;
  }
  .icon-badge { fill: var(--white); }
  .icon-slot { fill: var(--brand); opacity: 0.28; }
  .tax-ring { fill: url(#ringGradient); }
  .tax-disc { fill: var(--white); }
  .tax-label {
    fill: #111;
    font-weight: 800;
    font-size: 24px;
    letter-spacing: 1.6px;
  }
  .brand-name {
    fill: var(--ink);
    font-weight: 300;
    font-size: 62px;
    letter-spacing: 4px;
  }
  .brand-tagline {
    fill: var(--ink);
    font-weight: 400;
    font-size: 19px;
    letter-spacing: 2.4px;
  }
</style>
</head>
<body>
<svg class="artboard" viewBox="0 0 1280 1281" preserveAspectRatio="none" xmlns="http://www.w3.org/2000/svg">
  <defs>
    <linearGradient id="ringGradient" x1="0" y1="0" x2="1" y2="1">
      <stop offset="0" stop-color="#0c8a74"/>
      <stop offset="0.45" stop-color="#06a585"/>
      <stop offset="1" stop-color="#0d4f5a"/>
    </linearGradient>
  </defs>

  <g class="tax-pillars">
    <rect class="pillar-dark" x="77" y="400" width="104" height="565"/>
    <rect class="pillar-mid" x="181" y="470" width="105" height="335"/>
    <rect class="pillar-light" x="286" y="420" width="102" height="225"/>
  </g>

  <g class="level-bands">
    <path class="band-base" d="M620 847 H1146 A87 87 0 0 1 1146 1021 H620 Z"/>
    <path class="band-mid" d="M500 663 H1022 A87 87 0 0 1 1022 838 H500 Z"/>
    <path class="band-top" d="M388 480 H895 A87 87 0 0 1 895 655 H388 Z"/>
  </g>

  <g class="pyramid">
    <polygon class="face face-base-left" points="180,807 357,930 342,1148 78,962"/>
    <polygon class="face face-base-front" points="357,930 638,845 758,1022 342,1148"/>
    <polygon class="face face-mid-left" points="288,645 373,700 357,930 180,807"/>
    <polygon class="face face-mid-front" points="373,700 512,662 638,845 357,930"/>
    <polygon class="face face-top-left" points="385,485 373,700 288,645"/>
    <polygon class="face face-top-front" points="385,485 512,662 373,700"/>
    <polyline class="tier-seam" points="180,807 357,930 638,845"/>
    <polyline class="tier-seam" points="288,645 373,700 512,662"/>
  </g>

  <g class="tier-notes">
    <text class="tier-note" transform="translate(392 612) rotate(-20)">
      <tspan x="0" dy="0">Trusts,</tspan>
      <tspan x="-4" dy="20">Charity,</tspan>
      <tspan x="-2" dy="20">Bus. Exit</tspan>
      <tspan x="-2" dy="20">Planning</tspan>
    </text>
    <text class="tier-note" text-anchor="middle" transform="translate(488 836) rotate(-17)">
      <tspan x="0" dy="0">Investment,</tspan>
      <tspan x="0" dy="20">Retirement,</tspan>
      <tspan x="0" dy="20">Education Planning</tspan>
    </text>
    <text class="tier-note" text-anchor="middle" transform="translate(552 1032) rotate(-20)">
      <tspan x="0" dy="0">Emergency Savings,</tspan>
      <tspan x="0" dy="20">Insurance Coverage,</tspan>
      <tspan x="0" dy="20">Executed Wills</tspan>
    </text>
  </g>

  <g class="band-item">
    <circle class="icon-badge" cx="557" cy="568" r="44"/>
    <circle class="icon-slot" cx="557" cy="568" r="26" role="img" aria-label="Wealth distribution icon: money bag and gold bars"/>
    <text class="band-label" x="630" y="576">WEALTH DISTRIBUTION</text>
  </g>
  <g class="band-item">
    <circle class="icon-badge" cx="683" cy="751" r="44"/>
    <circle class="icon-slot" cx="683" cy="751" r="26" role="img" aria-label="Growing wealth icon: coin stack and sprouting plant"/>
    <text class="band-label" x="756" y="759">GROWING WEALTH</text>
  </g>
  <g class="band-item">
    <circle class="icon-badge" cx="808" cy="935" r="44"/>
    <circle class="icon-slot" cx="808" cy="935" r="26" role="img" aria-label="Protection icon: shield over briefcase and cash"/>
    <text class="band-label" x="881" y="932">PROTECTION</text>
    <text class="band-label" x="881" y="959">(RISK MANAGEMENT)</text>
  </g>

  <g class="tax-badge">
    <circle class="tax-ring" cx="232" cy="323" r="185"/>
    <circle class="tax-disc" cx="232" cy="323" r="156"/>
    <rect class="icon-slot" x="178" y="245" width="104" height="104" rx="16" role="img" aria-label="Tax planning icon: calculator, document and coin"/>
    <text class="tax-label" x="232" y="397" text-anchor="middle">TAX PLANNING</text>
  </g>

  <g class="brand">
    <text class="brand-name" x="452" y="318">corvalle</text>
    <text class="brand-tagline" x="456" y="354">PRIVATE ADVISORS</text>
  </g>
</svg>
</body>
</html>
```